Rack Card Design for an Ayurvedic Beauty Product Project

Hello, I need to have rack cards. The rack cards would be about 3 products we are showcasing at an event. I am a cosmetic company. I have a logo and basic design ideas. I have attached some product images and info. By no means am I a designer so please excuse my messy AI files. Please feel free to design this as feminine as you like. :)

Target Market(s)

Beauty industry, organic, holistic, ayurveda

Industry/Entity Type

Cosmetic

```html
<!DOCTYPE html>
<html lang="en">
<head>
<meta charset="utf-8">
<title>Gilt Lotus Rack Cards</title>
<link rel="stylesheet" href="https://fonts.googleapis.com/css2?family=Jost:wght@300;400;600&family=Pinyon+Script&display=swap">
<style>
  :root {
    --backdrop: #946b3e;
    --plum-top: #8c2b68;
    --plum-bottom: #570d3e;
    --plum-ink: #7a2058;
    --gold: #d2a766;
    --gold-dark: #9a6a3a;
    --gold-light: #e2b97a;
    --text-light: #ffffff;
  }
  * { margin: 0; padding: 0; box-sizing: border-box; }
  html, body { width: 1200px; height: 1145px; overflow: hidden; background: var(--backdrop); }
  body { position: relative; font-family: "Jost", sans-serif; color: var(--text-light); }

  .rack-card {
    position: absolute; top: 100px; width: 412px; height: 930px;
    background: linear-gradient(135deg, var(--gold-light), var(--gold-dark) 60%, var(--gold-light));
    box-shadow: 0 2px 8px rgba(0,0,0,0.35);
  }
  .rack-card--front { left: 152px; }
  .rack-card--back { left: 615px; }
  .card-face {
    position: absolute; left: 12px; top: 12px; width: 388px; height: 906px;
    background: linear-gradient(180deg, var(--plum-top), var(--plum-bottom));
    overflow: hidden;
  }

  /* front */
  .brand-mark { position: absolute; left: 0; top: 52px; width: 100%; text-align: center; }
  .brand-mark__dot { display: block; width: 110px; height: 110px; margin: 0 auto 18px; border-radius: 50%; background: var(--gold); }
  .brand-mark__name { font-size: 28px; font-weight: 400; color: var(--gold); letter-spacing: 1px; }

  .title-band {
    position: absolute; left: 0; top: 258px; width: 100%; height: 173px;
    background: linear-gradient(90deg, var(--gold-dark), var(--gold-light) 55%, #b98649);
    text-align: center;
  }
  .title-band__brand { margin-top: 14px; font-size: 31px; font-weight: 600; color: var(--plum-ink); letter-spacing: 1px; }
  .title-band__product { margin-top: 10px; font-size: 26px; font-weight: 300; line-height: 30px; color: var(--text-light); }

  .brand-story {
    position: absolute; left: 20px; top: 490px; width: 348px;
    font-size: 18px; line-height: 22.3px; text-align: center;
  }

  /* back */
  .product { position: absolute; }
  .product__name {
    font-family: "Pinyon Script", cursive; font-size: 28px; line-height: 31px;
    color: var(--gold); text-align: center;
  }
  .product__copy { margin-top: 8px; font-size: 18px; line-height: 22px; text-align: center; }
  .product--toner { left: 0; top: 30px; width: 270px; }
  .product--cream { left: 128px; top: 300px; width: 260px; }
  .product--serum { left: 0; top: 542px; width: 296px; }

  .product-shot { position: absolute; }
  .product-shot--toner { left: 259px; top: 41px; width: 104px; height: 214px; border-radius: 6px 6px 14px 14px; background: linear-gradient(90deg, #7d1f5a, #a4407c 45%, #6b1449); }
  .product-shot--cream { left: 27px; top: 320px; width: 121px; height: 180px; border-radius: 16px; background: linear-gradient(180deg, #d7b272 0 18%, #f1f1f1 18% 100%); }
  .product-shot--serum { left: 280px; top: 558px; width: 77px; height: 245px; border-radius: 6px 6px 12px 12px; background: linear-gradient(90deg, #7d1f5a, #a4407c 45%, #6b1449); }

  .social-row { position: absolute; left: 45px; top: 832px; width: 300px; height: 34px; }
  .social-row__rule { position: absolute; top: 16px; width: 88px; height: 1px; background: var(--gold); }
  .social-row__rule--left { left: 0; }
  .social-row__rule--right { right: 0; }
  .social-row__icon { position: absolute; top: 0; width: 33px; height: 33px; border-radius: 50%; background: var(--gold); }
</style>
</head>
<body>

<section class="rack-card rack-card--front">
  <div class="card-face">
    <div class="brand-mark">
      <span class="brand-mark__dot"></span>
      <span class="brand-mark__name">Gilt Lotus</span>
    </div>
    <div class="title-band">
      <h1 class="title-band__brand">GILT LOTUS</h1>
      <p class="title-band__product">Ayurvedic<br>Firming &amp; Lifting<br>Breast Cream</p>
    </div>
    <p class="brand-story">Gilt Lotus curates organic infused<br>products where holistic skin care meets a<br>luxurious experience. Each ingredient is<br>carefully selected; providing Ayurvedic<br>herbs, rich minerals &amp; elements. Stimu-<br>lating hydration and anti-oxidants to lift,<br>firm and illuminate your skin. We<br>believe in connecting with your inner<br>mantra, stimulating higher vibrations,<br>self-esteem, positive mind and soul. As a<br>brand we work with our<br>experts/suppliers of Ayurveda to ensure<br>that our products meet the quality,<br>wholesome healing<br>that you need.</p>
  </div>
</section>

<section class="rack-card rack-card--back">
  <div class="card-face">
    <div class="product product--toner">
      <h2 class="product__name">Gilt Lotus Firming &amp;<br>Lifting Breast Toner</h2>
      <p class="product__copy">Using all natural Ayurvedic<br>herbs, our breast toner,<br>prepares the area for<br>maximum absorption, giving<br>you the best results and the<br>most invigorating<br>treatment</p>
    </div>
    <div class="product-shot product-shot--toner" role="img" aria-label="Product photo of the breast toner tube with gold cap"></div>

    <div class="product-shot product-shot--cream" role="img" aria-label="Product photo of the breast cream jar with gold lid"></div>
    <div class="product product--cream">
      <h2 class="product__name">Gilt Lotus Firming &amp;<br>Lifting Breast Cream</h2>
      <p class="product__copy">Using all natural<br>Ayurvedic herbs, our<br>breast cream helps<br>enhance, tighten,<br>and lift your breast</p>
    </div>

    <div class="product product--serum">
      <h2 class="product__name">Gilt Lotus Firming and<br>Toning Breast Serum</h2>
      <p class="product__copy">Using all natural Ayurvedic<br>herbs, and a touch of 24k<br>gold, our serum enhances the<br>experience and quality of<br>results when partnered with<br>the Gilt Lotus Firming and<br>Lifting Breast Cream providing<br>an all-dayboosting experience</p>
    </div>
    <div class="product-shot product-shot--serum" role="img" aria-label="Product photo of the breast serum tube with gold cap"></div>

    <div class="social-row">
      <span class="social-row__rule social-row__rule--left"></span>
      <span class="social-row__icon" style="left:96px" aria-label="Social link"></span>
      <span class="social-row__icon" style="left:133px" aria-label="Social link"></span>
      <span class="social-row__icon" style="left:170px" aria-label="Social link"></span>
      <span class="social-row__rule social-row__rule--right"></span>
    </div>
  </div>
</section>

</body>
</html>
```